Two Separate Canvas Posters 54"width x 36" Height

I need two (2) posters designed for a new restaurant concept called: Lumar Crisp Wrap Kitchen.
Both posters will be printed on Canvas and placed into our new restaurants dining area.
I want this to look hip and cool.
I want so see red colors and earth tones. Please see attached for some ideas that I have.
The final design should communicate that you really gotta have this product and that this is a fun and casual place for a quick bite on the go.
Poster 1 message: gotta Eatta pita!
Size: 54"width x 36" high
Idea: Please see attached for design ideas and colors that I would like to see. If you can come up with any better idea, I would love to see this.
Poster 2 message: Power to the Pita
Size: 54"width x 36" height
Idea: Please see attached for design idea and colors that I want to see.
Restaurant

```html
<!DOCTYPE html>
<html lang="en">
<head>
<meta charset="utf-8">
<title>Power to the Pita — Lumar Crisp Wrap Kitchen</title>
<link rel="stylesheet" href="https://fonts.googleapis.com/css2?family=Poppins:wght@500;600&display=swap">
<style>
  :root {
    --ray-deep: #2e0207;
    --ray-dark: #420510;
    --ray-mid: #5a0a14;
    --ray-bright: #7c0f1c;
    --headline-orange: #f5a21f;
    --connector-orange: #d66f14;
    --hero-orange: #f7a83e;
    --bread-light: #f0d99a;
    --bread-mid: #ddbb6a;
    --bread-edge: #b98f45;
  }
  html, body {
    margin: 0;
    padding: 0;
    width: 1200px;
    height: 800px;
    overflow: hidden;
    background: var(--ray-deep);
  }
  .poster {
    position: relative;
    width: 1200px;
    height: 800px;
    overflow: hidden;
  }
  .artboard {
    position: absolute;
    inset: 0;
    width: 1200px;
    height: 800px;
  }
  .headline-text {
    font-family: "Poppins", "Century Gothic", sans-serif;
    font-weight: 600;
    filter: drop-shadow(2px 3px 0 rgba(40, 4, 0, 0.55)) drop-shadow(3px 5px 6px rgba(0, 0, 0, 0.4));
  }
  .word-power { fill: var(--headline-orange); font-size: 240px; }
  .word-to-the { fill: var(--connector-orange); font-size: 128px; }
  .word-pit { fill: var(--hero-orange); font-size: 430px; }
  .pita-photo {
    position: absolute;
    left: 742px;
    top: 222px;
    width: 342px;
    height: 290px;
    border-radius: 46% 44% 48% 46% / 40% 40% 56% 56%;
    background: radial-gradient(ellipse at 45% 45%, var(--bread-light) 0%, var(--bread-mid) 70%, var(--bread-edge) 100%);
    box-shadow: 4px 6px 12px rgba(0, 0, 0, 0.5);
  }
</style>
</head>
<body>
  <main class="poster">
    <svg class="artboard" viewBox="0 0 1200 800">
      <g class="sunburst" aria-hidden="true">
        <rect width="1200" height="800" fill="var(--ray-dark)"/>
        <polygon points="880,380 1200,-40 1200,150" fill="var(--ray-mid)"/>
        <polygon points="880,380 1200,300 1200,420" fill="var(--ray-bright)"/>
        <polygon points="880,380 1200,560 1200,700" fill="var(--ray-mid)"/>
        <polygon points="880,380 1130,800 1000,800" fill="var(--ray-deep)"/>
        <polygon points="880,380 930,800 840,800" fill="var(--ray-bright)"/>
        <polygon points="880,380 720,800 600,800" fill="var(--ray-mid)"/>
        <polygon points="880,380 430,800 300,800" fill="var(--ray-deep)"/>
        <polygon points="880,380 0,700 0,800 80,800" fill="var(--ray-mid)"/>
        <polygon points="880,380 0,470 0,560" fill="var(--ray-deep)"/>
        <polygon points="880,380 0,240 0,360" fill="var(--ray-bright)"/>
        <polygon points="880,380 0,0 180,0" fill="var(--ray-mid)"/>
        <polygon points="880,380 420,0 560,0" fill="var(--ray-deep)"/>
        <polygon points="880,380 820,0 920,0" fill="var(--ray-bright)"/>
        <polygon points="880,380 1020,0 1120,0" fill="var(--ray-deep)"/>
      </g>
      <g class="headline" role="heading" aria-level="1">
        <text class="headline-text word-power" transform="translate(112 450) rotate(-26)" textLength="600" lengthAdjust="spacingAndGlyphs">Power</text>
        <text class="headline-text word-to-the" transform="translate(282 502) rotate(-38)" textLength="350" lengthAdjust="spacingAndGlyphs">to the</text>
        <text class="headline-text word-pit" transform="translate(392 768) rotate(-30)" textLength="480" lengthAdjust="spacingAndGlyphs">pit</text>
      </g>
    </svg>

    <div class="pita-photo" role="img" aria-label="Photo of a round pita bread standing in for the letter a"></div>
  </main>
</body>
</html>
```